Company or website name
- Peter Holm, Inc. www.peterholminc-example.net
- Links to the website
- We are aged/seasoned corporation brokers who assist businesses to secure business loan financing
- Other Facts

```html
<!DOCTYPE html>
<html lang="en">
<head>
<meta charset="utf-8">
<title>Peter Holm, Inc.</title>
<link href="https://fonts.googleapis.com/css2?family=Source+Sans+3:wght@400;600&display=swap" rel="stylesheet">
<style>
  :root {
    --nav-top: #e4e4e4;
    --nav-bottom: #a9a9a9;
    --nav-divider: #8f8f8f;
    --nav-text: #333333;
    --band-light: #ffffff;
    --band-grey: #bdbdbd;
    --deep-navy: #012341;
    --teal: #056985;
    --panel: #ffffff;
    --body-text: #666666;
    --address-text: #555555;
    --heading-text: #333333;
    --footer-bg: #cccccc;
    --footer-text: #333333;
    --tab-dark: #2e2e30;
    --tab-mid: #6a6a6e;
    --hero-blue: #0a4fb0;
    --hero-light: #e9e6e0;
  }
  * { box-sizing: border-box; margin: 0; padding: 0; }
  html, body { width: 1200px; height: 1100px; overflow: hidden; }
  body {
    position: relative;
    font-family: "Source Sans 3", sans-serif;
    background:
      linear-gradient(to bottom, var(--nav-top) 0, #c6c6c6 53px, var(--band-light) 53px, var(--band-grey) 266px, var(--deep-navy) 266px, var(--teal) 760px, var(--teal) 1100px);
  }
  .site-nav {
    position: absolute; left: 188px; top: 3px; width: 830px; height: 50px;
    display: flex;
    background: linear-gradient(to bottom, var(--nav-top), var(--nav-bottom));
  }
  .site-nav a {
    width: 126px; display: flex; align-items: center; justify-content: center;
    color: var(--nav-text); text-decoration: none; font-size: 14px;
    border-right: 1px solid var(--nav-divider);
    box-shadow: 1px 0 0 #d8d8d8;
  }
  .site-nav .nav-phone {
    flex: 1; border-right: none; box-shadow: none;
    font-size: 16px; font-weight: 600; color: #3a3a3a;
  }
  .hero {
    position: absolute; left: 188px; top: 68px; width: 830px; height: 275px;
    background: linear-gradient(100deg, #0837a0 0%, var(--hero-blue) 25%, #b9cbe0 45%, var(--hero-light) 70%, #d9d4cc 100%);
  }
  .page-panel {
    position: absolute; left: 190px; top: 343px; width: 828px; height: 647px;
    background: var(--panel);
  }
  .brand-tab { position: absolute; left: 188px; top: 343px; }
  .brand-name {
    position: absolute; left: 225px; top: 345px;
    font-size: 37px; font-weight: 400; color: #ffffff; letter-spacing: -0.5px;
  }
  .main-copy {
    position: absolute; left: 221px; top: 440px; width: 470px;
    font-size: 14.5px; line-height: 17.5px; color: var(--body-text);
    text-align: justify;
  }
  .main-copy p { margin-bottom: 17.5px; }
  .search-box {
    position: absolute; left: 730px; top: 370px; width: 253px; height: 30px;
    border-bottom: 2px solid #d4d4d4; border-left: 1px solid #eeeeee;
    background: linear-gradient(to bottom, #ffffff, #f2f2f2);
    font-size: 14px; color: #333; padding: 7px 0 0 23px;
  }
  .search-box svg { position: absolute; right: 9px; top: 8px; }
  .address {
    position: absolute; left: 754px; top: 436px; width: 230px;
    font-size: 14px; line-height: 17.5px; color: var(--address-text);
    font-style: normal; text-transform: uppercase;
  }
  .side-heading {
    position: absolute; left: 730px; width: 253px; height: 30px;
    background: linear-gradient(to bottom, #ffffff, #dcdcdc);
    border-bottom: 2px solid #c9c9c9;
    font-size: 14px; color: var(--heading-text); padding: 6px 0 0 27px;
    text-transform: uppercase; font-weight: 400;
  }
  .side-copy {
    position: absolute; left: 745px; width: 229px;
    font-size: 14.5px; line-height: 17.5px; color: var(--body-text);
    text-align: justify;
  }
  .side-copy p { margin-bottom: 17.5px; }
  .site-footer {
    position: absolute; left: 190px; top: 990px; width: 828px; height: 76px;
    background: var(--footer-bg);
    display: flex; align-items: center; justify-content: center;
    font-size: 11.5px; letter-spacing: 0.6px; color: var(--footer-text);
  }
</style>
</head>
<body>
  <nav class="site-nav">
    <a href="#">HOME</a>
    <a href="#">ABOUT</a>
    <a href="#">SERVICES</a>
    <a href="#">FAQ</a>
    <a href="#">CONTACT</a>
    <span class="nav-phone">323.555.0148</span>
  </nav>

  <div class="hero" role="img" aria-label="Photo of a smiling team of business brokers in suits standing in an office lobby, over a blue financial grid with a rising chart line"></div>

  <div class="page-panel"></div>

  <svg class="brand-tab" width="460" height="62" viewBox="0 0 460 62" aria-hidden="true">
    <defs>
      <linearGradient id="tabFill" x1="0" y1="0" x2="0" y2="1">
        <stop offset="0" stop-color="#8a8a8e"/>
        <stop offset="0.35" stop-color="#3c3c40"/>
        <stop offset="1" stop-color="var(--tab-dark)"/>
      </linearGradient>
    </defs>
    <path d="M0 0 H450 C410 30 370 52 300 56 H0 Z" fill="url(#tabFill)"/>
    <path d="M0 56 H300 C370 52 410 30 450 0 L452 0 C412 32 372 58 300 60 H0 Z" fill="#bdbdbd"/>
  </svg>
  <div class="brand-name">PETER HOLM INC</div>

  <main class="main-copy">
    <p>Lorem ipsum dolor sit amet, consectetuer adipiscing elit. Nam cursus. Morbi ut mi. Nullam enim leo, egestas id, condimentum at, laoreet mattis, massa. Sed eleifend nonummy diam. Praesent mauris ante, elementum et, bibendutm at, posuere sit amet, nibh. Duis tincidunt lectus quis dui viverra vestibulum. Suspendisse vulputate aliquam dui. Nulla elementum dui ut augue.</p>
    <p>Aliquam vehicula mi at mauris. Maecenas placerat, nisl at consequat rhoncus, sem nunc gravida justo, quis eleifend arcu velit quis lacus. Morbi magna magna, tincidunt a, mattis non, imperdiet vitae, tellus. Sed odio est, auctor ac, sollicitudin in, consequat vitae, orci. Fusce id felis. Vivamus sollicitudin metus eget eros.</p>
    <p>Pellentesque habitant morbi tristique senectus et netus et malesuada fames ac turpis egestas. In posuere felis nec tortor. Pellentesque faucibus. Ut accumsan ultricies elit. Maecenas at justo id velit placerat molestie. Donec dictum lectus non odio. Cras a ante vitae enim iaculis aliquam. Mauris nunc quam, venenatis nec, euismod sit amet, egestas placerat, est. Pellentesque habitant morbi tristique senectus et netus et malesuada fames ac turpis egestas. Cras id elit. Integer quis urna. Ut ante enim, dapibus malesuada, fringilla eu, condimentum quis, tellus. Aenean porttitor eros vel dolor. Donec convallis pede venenatis nibh. Duis quam. Nam eget lacus. Aliquam erat volutpat. Quisque dignissim congue leo.</p>
  </main>

  <div class="search-box">SEARCH
    <svg width="14" height="14" viewBox="0 0 14 14" aria-hidden="true">
      <circle cx="5.5" cy="5.5" r="4" fill="none" stroke="#777" stroke-width="2"/>
      <line x1="8.5" y1="8.5" x2="13" y2="13" stroke="#777" stroke-width="2.5" stroke-linecap="round"/>
    </svg>
  </div>

  <address class="address">
    Peter Holm Inc.<br>
    118 North Alder Crest Avenue,<br>
    Suite 402<br>
    Lakemont, CA. 90377<br>
    Tel:&nbsp; 323.555.0148<br>
    Fax: 323.555.0193
  </address>

  <h2 class="side-heading" style="top:577px">What's new this week?</h2>
  <div class="side-copy" style="top:626px">
    <p>Lorem ipsum dolor sit amet, consectetuer adipiscing elit. Nam cursus. Morbi ut mi.</p>
    <p>Nullam enim leo, egestas id, condimentum at, laoreet mattis, massa. Sed eleifend nonummy diam.</p>
  </div>

  <h2 class="side-heading" style="top:769px">Free Reports</h2>
  <div class="side-copy" style="top:821px">
    <p>Lorem ipsum dolor sit amet, consectetuer adipiscing elit. Nam cursus. Morbi ut mi.</p>
    <p>Nullam enim leo, egestas id, condimentum at, laoreet mattis, massa. Sed eleifend nonummy diam.</p>
  </div>

  <footer class="site-footer">COPYRIGHT © 2011 PETER HOLM, INC. ALL RIGHTS RESERVED.</footer>
</body>
</html>
```